hi all

Im after a new age looking business card with my company logo on it

must include these details, I would like the PH and Email to be symbols

If the colours used for card could be kept within the colours used in logo that I have supplied that would be great, if another colour is to be used dark grey would be ok. no light bulbs etc thanks

Details below to be incorporated on card

Damian Holloway

Lic E871302

PH 0219647381

E info@brightvaleelectrical.example.nz

Domestic Commercial Industrial Electricians

```html
<!DOCTYPE html>
<html lang="en">
<head>
<meta charset="utf-8">
<title>Brightvale Electrical – Business Card</title>
<link href="https://fonts.googleapis.com/css2?family=Lato:wght@400;700&family=Montserrat:wght@700;800&display=swap" rel="stylesheet">
<style>
  :root{
    --brand-blue:#1774c1;
    --ink:#1d1d1d;
    --paper:#ffffff;
    --backdrop:#2a2a2a;
  }
  *{margin:0;padding:0;box-sizing:border-box}
  html,body{width:1200px;height:1159px;overflow:hidden;background:var(--backdrop)}
  .canvas{position:relative;width:1200px;height:1159px}
  .card{position:absolute;left:120px;width:960px;height:536px;box-shadow:0 12px 28px rgba(0,0,0,.45)}
  .card--front{top:30px;background:var(--paper)}
  .card--back{top:593px;background:var(--brand-blue)}

  .wordmark{position:absolute;display:flex;flex-direction:column;align-items:center;font-family:"Montserrat",sans-serif;font-weight:800;text-transform:uppercase;line-height:1}
  .wordmark__mark{width:96px;height:96px;border-radius:50%;margin-bottom:18px}
  .wordmark__name{font-size:44px;letter-spacing:1px}
  .wordmark__sub{font-size:20px;letter-spacing:5px;margin-top:8px}

  .card--front .wordmark{left:70px;top:150px;width:380px;color:var(--brand-blue)}
  .card--front .wordmark__mark{background:var(--brand-blue)}
  .card--back .wordmark{left:0;right:0;top:150px;color:var(--paper)}
  .card--back .wordmark__mark{background:var(--paper)}
  .card--back .wordmark__name{font-size:62px}
  .card--back .wordmark__sub{font-size:26px;letter-spacing:7px}

  .divider{position:absolute;left:480px;top:165px;width:2px;height:204px;background:var(--ink)}

  .contact{position:absolute;left:503px;top:170px;font-family:"Lato",sans-serif;color:var(--ink)}
  .contact__name{font-family:"Montserrat",sans-serif;font-weight:700;font-size:31px;color:var(--brand-blue);text-transform:uppercase;line-height:1.1}
  .contact__licence{font-size:24px;margin-top:4px}
  .contact__list{list-style:none;margin-top:26px}
  .contact__item{display:flex;align-items:center;gap:9px;font-size:24px;line-height:38px}
  .contact__icon{width:22px;height:22px;flex:none;fill:var(--brand-blue)}

  .tagline{position:absolute;left:92px;right:92px;top:464px;display:flex;align-items:center;gap:14px;font-family:"Lato",sans-serif;font-size:24px;color:var(--ink);white-space:nowrap}
  .tagline::before,.tagline::after{content:"";flex:1;height:2px;background:var(--brand-blue)}
</style>
</head>
<body>
<main class="canvas">
  <section class="card card--front" aria-label="Business card front">
    <div class="wordmark">
      <span class="wordmark__mark"></span>
      <span class="wordmark__name">Brightvale</span>
      <span class="wordmark__sub">Electrical</span>
    </div>
    <div class="divider"></div>
    <div class="contact">
      <p class="contact__name">Damian Holloway</p>
      <p class="contact__licence">Lic E871302</p>
      <ul class="contact__list">
        <li class="contact__item">
          <svg class="contact__icon" viewBox="0 0 24 24" aria-hidden="true"><path d="M6.6 10.8a15 15 0 0 0 6.6 6.6l2.2-2.2c.3-.3.7-.4 1-.2 1.1.4 2.3.6 3.6.6.6 0 1 .4 1 1V20c0 .6-.4 1-1 1A17 17 0 0 1 3 4c0-.6.4-1 1-1h3.5c.6 0 1 .4 1 1 0 1.3.2 2.5.6 3.6.1.3 0 .7-.2 1z"/></svg>
          <span>0219647381</span>
        </li>
        <li class="contact__item">
          <svg class="contact__icon" viewBox="0 0 24 24" aria-hidden="true"><path d="M2 5h20v14H2zm2 2v.5l8 5 8-5V7l-8 5z"/></svg>
          <span>info@brightvaleelectrical.example.nz</span>
        </li>
        <li class="contact__item">
          <svg class="contact__icon" viewBox="0 0 24 24" aria-hidden="true"><path d="M12 2a10 10 0 1 0 0 20 10 10 0 0 0 0-20zm-1 17.9A8 8 0 0 1 4.1 10L9 15v1a2 2 0 0 0 2 2zm6.9-2.5A2 2 0 0 0 16 16h-1v-3a1 1 0 0 0-1-1H8v-2h2a1 1 0 0 0 1-1V7h2a2 2 0 0 0 2-2v-.4a8 8 0 0 1 2.9 12.8z"/></svg>
          <span>www.brightvaleelectrical.co.nz</span>
        </li>
      </ul>
    </div>
    <p class="tagline">Domestic Commercial Industrial Electricians</p>
  </section>

  <section class="card card--back" aria-label="Business card back">
    <div class="wordmark">
      <span class="wordmark__mark"></span>
      <span class="wordmark__name">Brightvale</span>
      <span class="wordmark__sub">Electrical</span>
    </div>
  </section>
</main>
</body>
</html>
```